property investment and development company needs a website

we need a website that looks professional and portrays trust for people looking to us to buy their house or investors looking to invest or joint venture with us.
We are based in the west midlands in the UK.
we deal mainly with residential housing, house to flats conversions, HMO's (houses in multiple ocupancy).
we require the website as a first point of contact with potential sellers, renters and investors so links or contact details that are easy to access or see would be good.
I have had logos designed by a plan hollow member and these can be used as guidance for the colour and style of the site.
Target Market(s)
joint venture investment partners, people looking to sell their house, people looking to rent from us.
Coding
Coded - Design and coding required
Number of Pages Required
3 page
Requirements
Must have
- project a professional appearance
- visable contact details

```html
<!DOCTYPE html>
<html lang="en">
<head>
<meta charset="utf-8">
<title>Hartwell Homes – Property Investment &amp; Development, West Midlands</title>
<link href="https://fonts.googleapis.com/css2?family=Marcellus&family=Montserrat:wght@400;500;600;700&display=swap" rel="stylesheet">
<style>
:root{
  --gold:#c9b78e;
  --ink:#2f3236;
  --text:#4a4d52;
  --muted:#a3a6aa;
  --line:#e6e6e6;
  --paper:#ffffff;
  --soft:#f6f6f6;
  --slate:#464a4d;
  --slate-deep:#3e4245;
  --serif:'Marcellus', Georgia, serif;
  --sans:'Montserrat', Arial, sans-serif;
}
*{box-sizing:border-box;margin:0;padding:0}
html,body{width:1200px;height:3337px;overflow:hidden}
body{position:relative;background:var(--paper);font-family:var(--sans);color:var(--text)}
.abs{position:absolute}

/* hero */
.hero{position:absolute;left:0;top:0;width:1200px;height:583px;
  background:linear-gradient(100deg,#3f5977 0%,#6f86a3 35%,#8a98ab 55%,#b7bec8 80%,#d9dbde 100%)}
.brand{position:absolute;left:83px;top:24px;display:flex;align-items:center;gap:12px}
.brand-mark{width:34px;height:34px;background:var(--gold)}
.brand-name{font-family:var(--serif);color:#fff;font-size:24px;line-height:26px;letter-spacing:1.5px;text-transform:uppercase}
.nav{position:absolute;left:385px;top:33px;display:flex}
.nav a{color:#fff;text-decoration:none;font-size:9px;font-weight:600;letter-spacing:1.2px;text-transform:uppercase;margin-right:26px;position:relative}
.nav a.active::after{content:"";position:absolute;left:0;right:0;top:16px;height:2px;background:var(--gold)}
.btn-visit{position:absolute;left:1030px;top:24px;width:135px;height:29px;border:2px solid var(--gold);color:#fff;
  font-size:9px;font-weight:700;letter-spacing:1.6px;text-transform:uppercase;display:flex;align-items:center;justify-content:center}
.hero-title{position:absolute;left:0;width:1200px;top:226px;text-align:center;font-family:var(--serif);font-weight:400;color:#fff;font-size:40px;line-height:49px;text-transform:uppercase}
.hero-sub{position:absolute;left:0;width:1200px;top:351px;text-align:center;color:#fff;font-size:10px;font-weight:600;line-height:17px;text-transform:uppercase}
.hours{position:absolute;left:83px;top:531px;color:#fff;font-size:8px;line-height:13px;text-transform:uppercase}
.hours b{font-weight:700}

/* section heading */
.sec-title{position:absolute;display:flex;align-items:center;gap:12px;font-family:var(--serif);font-weight:400;font-size:19px;color:var(--ink);text-transform:uppercase}
.sec-title.light{color:#fff}

/* who we are */
.lead{font-size:10px;line-height:16px;color:var(--ink)}
.body-copy{font-size:10px;line-height:16px;color:var(--muted)}
.ov-accent{left:838px;top:663px;width:131px;height:99px;background:var(--gold)}
.ov-photo{left:609px;top:670px;width:354px;height:266px;background:linear-gradient(180deg,#7f99b9 0%,#a6b9cc 45%,#6a5a4c 80%,#3e3a39 100%)}
.stat{position:absolute;top:992px;width:147px}
.stat-num{font-family:var(--serif);font-size:24px;color:var(--ink)}
.stat-label{font-size:7.5px;letter-spacing:.8px;color:var(--muted);text-transform:uppercase;margin-top:6px}
.stat-bar{height:6px;background:#f1f1f1;margin-top:16px}

/* services */
.services{left:4px;top:1121px;width:1196px;height:508px;background:var(--soft)}
.svc{position:absolute;width:232px;height:156px;background:#fff;padding:28px 22px 0 24px}
.svc-head{display:flex;align-items:center;gap:10px;height:30px}
.svc-head h3{font-family:var(--serif);font-weight:400;font-size:10px;line-height:12px;color:var(--ink);text-transform:uppercase}
.svc p{font-size:9px;line-height:16px;color:var(--muted);margin-top:12px}

/* property types */
.tabs{left:231px;top:1759px;width:738px;height:46px;display:flex;background:var(--soft)}
.tab{flex:1;display:flex;align-items:center;justify-content:center;text-align:center;font-size:8.5px;font-weight:600;letter-spacing:1.6px;line-height:11px;color:var(--ink);text-transform:uppercase;position:relative}
.tab.active{background:var(--gold);color:#fff}
.tab.active::after{content:"";position:absolute;bottom:-7px;left:50%;margin-left:-7px;border:7px solid transparent;border-bottom:0;border-top-color:var(--gold)}
.spec{left:231px;top:1945px;width:310px}
.spec-row{display:flex;justify-content:space-between;height:29px;align-items:center;border-bottom:1px solid var(--line);font-size:9px;color:var(--ink)}
.spec-row span:first-child{font-size:7.5px;color:var(--muted);text-transform:uppercase;letter-spacing:.4px}
.btn-outline{left:231px;top:2121px;width:310px;height:29px;border:2px solid var(--gold);color:var(--gold);font-size:8.5px;font-weight:700;letter-spacing:1.8px;display:flex;align-items:center;justify-content:center;text-transform:uppercase}
.plan-img{left:609px;top:1899px;width:360px;height:224px;background:#f3f3f3;border:3px solid #1e1e1e}

/* areas */
.hoods{left:0;top:2232px;width:1200px;height:574px;background:var(--slate)}
.acc{left:231px;top:2347px;width:246px;height:378px;background:#fff;padding:40px 30px 0 32px}
.acc-item{display:flex;justify-content:space-between;align-items:center;height:45px;border-bottom:1px solid var(--line);font-size:8.5px;font-weight:700;letter-spacing:1.6px;color:var(--ink);text-transform:uppercase}
.acc-item.open{color:var(--gold);border-bottom:0}
.acc-body{font-size:9px;line-height:16px;color:var(--muted);padding:4px 0 20px;border-bottom:1px solid var(--line)}
.acc-rail{left:457px;top:2389px;width:4px;height:316px;background:var(--gold)}
.aerial{left:477px;top:2347px;width:486px;height:378px;background:linear-gradient(170deg,#6e7264 0%,#4e5148 40%,#3a3d36 100%)}

/* contact */
.contact{left:0;top:2806px;width:1200px;height:531px;background:var(--slate-deep)}
.cta{position:absolute;left:0;width:1200px;text-align:center;font-family:var(--serif);color:#fff;text-transform:uppercase}
.col-head{position:absolute;top:2992px;font-size:8px;font-weight:700;letter-spacing:1.8px;color:var(--gold);text-transform:uppercase}
.foot-copy{font-size:9.5px;line-height:16px;color:#fff}
.info-row{position:absolute;left:231px;display:flex;font-size:9.5px;line-height:16px;color:#fff}
.info-row span:first-child{width:50px;font-size:7.5px;color:#9a9ea2;text-transform:uppercase}
.field{position:absolute;border:1px solid var(--gold);color:#b3b5b8;font-size:9px;padding:0 13px;display:flex;align-items:center}
.field.area{align-items:flex-start;padding-top:10px}
.submit{position:absolute;left:736px;top:3173px;width:233px;height:26px;background:#fff;color:var(--gold);font-size:8px;font-weight:700;letter-spacing:1.8px;display:flex;align-items:center;justify-content:center}
.legal{position:absolute;left:0;top:3263px;width:1200px;text-align:center;font-size:7px;color:#9a9ea2;letter-spacing:.3px;text-transform:uppercase}
.legal b{color:#fff}.legal em{font-style:normal;color:var(--gold)}
.social{position:absolute;left:545px;top:3292px;display:flex;gap:26px}
.social i{display:block;width:8px;height:8px;border-radius:50%;background:#8a8e92}
</style>
</head>
<body>

<header class="hero" role="img" aria-label="Upward view of tall buildings against a pale blue sky"></header>
<div class="brand"><span class="brand-mark"></span><span class="brand-name">Hartwell<br>Homes</span></div>
<nav class="nav">
  <a class="active" href="#">Home</a><a href="#">About Us</a><a href="#">Properties</a><a href="#">Blog</a><a href="#">Services</a><a href="#">Contact Us</a>
</nav>
<div class="btn-visit">Call us today</div>
<h1 class="hero-title">Property investment<br>across the West Midlands</h1>
<p class="hero-sub">We buy houses – we let quality homes –<br>we build with joint venture partners.</p>
<p class="hours">Office hours<br><b>Mon - Fri: 9am - 6pm / Sat: 10am - 2pm / Tel: 0000 555 0142</b></p>

<!-- who we are -->
<h2 class="sec-title" style="left:231px;top:697px">
  <svg width="12" height="6" viewBox="0 0 12 6"><g fill="#c9b78e"><rect x="0" y="0" width="2" height="2"/><rect x="3" y="0" width="2" height="2"/><rect x="6" y="0" width="2" height="2"/><rect x="9" y="0" width="2" height="2"/><rect x="0" y="4" width="2" height="2"/><rect x="3" y="4" width="2" height="2"/><rect x="6" y="4" width="2" height="2"/></g></svg>
  Who we are
</h2>
<p class="abs lead" style="left:231px;top:738px;width:300px">Hartwell Homes is a West Midlands property investment and development company working in residential housing, house to flat conversions and HMOs.</p>
<p class="abs body-copy" style="left:231px;top:806px;width:300px">We offer homeowners a fair, fast and no-fee sale, give tenants well-kept rooms and flats managed by a local team, and give investors clear, secured joint venture deals with regular reporting on every project.</p>
<div class="abs ov-accent"></div>
<div class="abs ov-photo" role="img" aria-label="Refurbished red brick terraced houses on a residential street"></div>

<div class="stat" style="left:231px"><div class="stat-num">340</div><div class="stat-label">Houses bought</div><div class="stat-bar"></div></div>
<div class="stat" style="left:428px"><div class="stat-num">126</div><div class="stat-label">Flats converted</div><div class="stat-bar"></div></div>
<div class="stat" style="left:625px"><div class="stat-num">58</div><div class="stat-label">HMOs managed</div><div class="stat-bar"></div></div>
<div class="stat" style="left:822px"><div class="stat-num">24</div><div class="stat-label">JV partners</div><div class="stat-bar"></div></div>

<!-- services -->
<section class="abs services" role="img" aria-label="Faint architectural plan linework across a light grey band"></section>
<h2 class="sec-title" style="left:236px;top:1173px">
  <svg width="12" height="6" viewBox="0 0 12 6"><g fill="#c9b78e"><rect x="0" y="0" width="2" height="2"/><rect x="3" y="0" width="2" height="2"/><rect x="6" y="0" width="2" height="2"/><rect x="9" y="0" width="2" height="2"/><rect x="0" y="4" width="2" height="2"/><rect x="3" y="4" width="2" height="2"/><rect x="6" y="4" width="2" height="2"/></g></svg>
  Our services
</h2>

<article class="svc" style="left:236px;top:1222px">
  <div class="svc-head"><svg width="26" height="26" viewBox="0 0 26 26" fill="none" stroke="#c9b78e" stroke-width="1.3"><path d="M3 12L13 4l10 8"/><path d="M6 10v12h14V10"/><path d="M11 22v-6h4v6"/></svg><h3>Sell your house<br>fast</h3></div>
  <p>A cash offer within 48 hours, no agent fees and a completion date that suits you and your family</p>
</article>
<article class="svc" style="left:487px;top:1222px">
  <div class="svc-head"><svg width="26" height="26" viewBox="0 0 26 26" fill="none" stroke="#c9b78e" stroke-width="1.3"><circle cx="9" cy="13" r="5"/><path d="M14 13h10M20 13v4M23 13v3"/></svg><h3>Rooms and flats<br>to rent</h3></div>
  <p>Furnished rooms and modern flats with bills options, fair rents and a local team on call</p>
</article>
<article class="svc" style="left:739px;top:1222px">
  <div class="svc-head"><svg width="26" height="26" viewBox="0 0 26 26" fill="none" stroke="#c9b78e" stroke-width="1.3"><path d="M2 12l5-5 6 3 6-3 5 5"/><path d="M7 13l5 5c1 1 2 1 3 0l4-4"/><path d="M2 12l5 6M24 12l-5 6"/></svg><h3>Joint venture<br>partnerships</h3></div>
  <p>Secured, transparent deals with shared returns, clear timelines and monthly project updates</p>
</article>
<article class="svc" style="left:236px;top:1398px">
  <div class="svc-head"><svg width="26" height="26" viewBox="0 0 26 26" fill="none" stroke="#c9b78e" stroke-width="1.3"><rect x="5" y="3" width="16" height="20"/><path d="M5 13h16M9 7h3M14 7h3M9 17h3M14 17h3"/></svg><h3>House to flat<br>conversions</h3></div>
  <p>We turn large houses into well planned self-contained flats, from planning through to letting</p>
</article>
<article class="svc" style="left:487px;top:1398px">
  <div class="svc-head"><svg width="26" height="26" viewBox="0 0 26 26" fill="none" stroke="#c9b78e" stroke-width="1.3"><circle cx="8" cy="9" r="3"/><circle cx="18" cy="9" r="3"/><path d="M2 21c1-5 11-5 12 0M12 21c1-5 11-5 12 0"/></svg><h3>HMO lettings<br>and management</h3></div>
  <p>Licensed, compliant shared homes with regular inspections and quick repairs for every tenant</p>
</article>
<article class="svc" style="left:739px;top:1398px">
  <div class="svc-head"><svg width="26" height="26" viewBox="0 0 26 26" fill="none" stroke="#c9b78e" stroke-width="1.3"><path d="M4 22l10-10"/><path d="M12 6l8 8 3-3-8-8z"/></svg><h3>Refurbishment<br>and development</h3></div>
  <p>Full refurbishments delivered by trusted local trades, on budget and to a high standard</p>
</article>

<!-- property types -->
<h2 class="sec-title" style="left:231px;top:1708px">
  <svg width="12" height="6" viewBox="0 0 12 6"><g fill="#c9b78e"><rect x="0" y="0" width="2" height="2"/><rect x="3" y="0" width="2" height="2"/><rect x="6" y="0" width="2" height="2"/><rect x="9" y="0" width="2" height="2"/><rect x="0" y="4" width="2" height="2"/><rect x="3" y="4" width="2" height="2"/><rect x="6" y="4" width="2" height="2"/></g></svg>
  Homes to rent
</h2>
<div class="abs tabs">
  <div class="tab active">HMO room</div><div class="tab">Studio</div><div class="tab">One bed<br>flat</div><div class="tab">Two bed flat</div><div class="tab">Family house</div>
</div>
<p class="abs lead" style="left:231px;top:1870px;width:300px">A converted Victorian house offering six en-suite rooms with a shared modern kitchen, lounge and garden, close to shops and transport links.</p>
<div class="abs spec">
  <div class="spec-row"><span>Location</span><span>Wolverhampton</span></div>
  <div class="spec-row"><span>Rooms</span><span>6</span></div>
  <div class="spec-row"><span>Total area, sq.m</span><span>145</span></div>
  <div class="spec-row"><span>Bills included</span><span>Yes</span></div>
  <div class="spec-row" style="border-bottom:0"><span>Rent</span><span>£520 pcm per room</span></div>
</div>
<div class="abs btn-outline">Enquire to rent</div>
<div class="abs plan-img" role="img" aria-label="Floor plan of a six room shared house with kitchen, lounge and bathrooms"></div>

<!-- areas -->
<section class="abs hoods" role="img" aria-label="Faint plan linework on a dark slate band"></section>
<h2 class="sec-title light" style="left:231px;top:2287px">
  <svg width="12" height="6" viewBox="0 0 12 6"><g fill="#ffffff"><rect x="0" y="0" width="2" height="2"/><rect x="3" y="0" width="2" height="2"/><rect x="6" y="0" width="2" height="2"/><rect x="9" y="0" width="2" height="2"/><rect x="0" y="4" width="2" height="2"/><rect x="3" y="4" width="2" height="2"/><rect x="6" y="4" width="2" height="2"/></g></svg>
  Areas we cover
</h2>
<div class="abs acc">
  <div class="acc-item"><span>Birmingham</span><svg width="7" height="5" viewBox="0 0 7 5"><path d="M1 1l2.5 2.5L6 1" fill="none" stroke="#2f3236" stroke-width="1.2"/></svg></div>
  <div class="acc-item open"><span>Wolverhampton</span><svg width="7" height="5" viewBox="0 0 7 5"><path d="M1 4l2.5-2.5L6 4" fill="none" stroke="#2f3236" stroke-width="1.2"/></svg></div>
  <div class="acc-body">Our busiest area for HMOs and conversions. We buy houses in any condition and have rooms and flats available to rent now.</div>
  <div class="acc-item"><span>Coventry</span><svg width="7" height="5" viewBox="0 0 7 5"><path d="M1 1l2.5 2.5L6 1" fill="none" stroke="#2f3236" stroke-width="1.2"/></svg></div>
  <div class="acc-item"><span>Walsall</span><svg width="7" height="5" viewBox="0 0 7 5"><path d="M1 1l2.5 2.5L6 1" fill="none" stroke="#2f3236" stroke-width="1.2"/></svg></div>
  <div class="acc-item" style="border-bottom:0"><span>Dudley</span><svg width="7" height="5" viewBox="0 0 7 5"><path d="M1 1l2.5 2.5L6 1" fill="none" stroke="#2f3236" stroke-width="1.2"/></svg></div>
</div>
<div class="abs acc-rail"></div>
<div class="abs aerial" role="img" aria-label="Aerial evening view of a West Midlands town with highlighted project locations"></div>

<!-- contact -->
<section class="abs contact"></section>
<p class="cta" style="top:2848px;font-size:18px">Selling, renting or investing?</p>
<p class="cta" style="top:2873px;font-size:29px">It's time to talk</p>
<p class="cta" style="top:2912px;font-size:17px">to our team</p>

<h4 class="col-head" style="left:231px">Our office</h4>
<h4 class="col-head" style="left:483px">Investor contact</h4>
<h4 class="col-head" style="left:736px">Enquire</h4>

<p class="abs foot-copy" style="left:231px;top:3022px;width:215px">Call, email or visit us. Sellers, tenants and investors all get a reply from our local team within one working day.</p>
<div class="info-row" style="top:3096px"><span>Address:</span><span>Unit 4, 18 Canal Street,<br>Halsworth, HW4 7QP</span></div>
<div class="info-row" style="top:3142px"><span>Phone:</span><span>0000 555 0142</span></div>
<div class="info-row" style="top:3171px"><span>E-mail:</span><span>hello@hartwellhomes.test</span></div>

<div class="abs" role="img" aria-label="Portrait of the investment manager" style="left:483px;top:3025px;width:54px;height:54px;border-radius:50%;background:#d6d3cf;border:3px solid #fff"></div>
<p class="abs" style="left:546px;top:3041px;font-family:var(--serif);color:#fff;font-size:11px;text-transform:uppercase">Thomas Pell</p>
<p class="abs" style="left:546px;top:3062px;font-size:7px;color:#9a9ea2;letter-spacing:.6px;text-transform:uppercase">Investment manager</p>
<div class="abs" style="left:483px;top:3100px;width:172px;height:1px;background:#5a5e62"></div>
<div class="abs" style="left:486px;top:3119px;display:flex;gap:13px;align-items:center;font-size:9.5px;color:#fff">
  <svg width="9" height="9" viewBox="0 0 10 10"><path d="M2 1l2 2-1 1.5c.7 1.4 1.6 2.3 3 3L7.5 6l2 2-1.5 1.5C4.5 9 1 5.5.5 2.5z" fill="#9a9ea2"/></svg>0000 555 0178</div>
<div class="abs" style="left:486px;top:3140px;display:flex;gap:13px;align-items:center;font-size:9.5px;color:#fff">
  <svg width="9" height="7" viewBox="0 0 10 8"><rect width="10" height="8" fill="#9a9ea2"/><path d="M0 0l5 4 5-4" fill="none" stroke="#3e4245" stroke-width="1"/></svg>invest@hartwellhomes.test</div>

<div class="field" style="left:736px;top:3024px;width:113px;height:28px">Your name *</div>
<div class="field" style="left:857px;top:3024px;width:112px;height:28px">Phone number</div>
<div class="field" style="left:736px;top:3062px;width:233px;height:28px">Your e-mail *</div>
<div class="field area" style="left:736px;top:3100px;width:233px;height:62px">Selling, renting or investing?</div>
<div class="submit">Submit</div>

<p class="legal"><b>© Hartwell Homes.</b> All rights reserved. <em>Terms of use</em> and <em>Privacy policy</em></p>
<div class="social"><i></i><i></i><i></i><i></i></div>

</body>
</html>
```